Senior sex novelty store providing a private method for acquiring the products and knowledge

Our business supplies novelty sex products and services, specializing in the 50+ demographic. Products include sex products for individuals and couples. Services include webinars and teleseminars that address various sex and relationship issues. We are dedicated to providing discreet delivery of products and knowledge to people over 50 entering a new phase of life, facing new challenges. Our entire process from site through shipping is kept private to allow our customers the freedom to shop and learn in the privacy of their own home.

Target Market(s)

Seniors over 50 years old

Industry/Entity Type

Store

Number of Pages Required

1 page

Font styles to use
Serif

Requirements
Must have
• place for business description with a private look
Should not have
• anything sleazy

```html
<!DOCTYPE html>
<html lang="en">
<head>
<meta charset="utf-8">
<title>Quiet Chapter — Private Store for Life After 50</title>
<link href="https://fonts.googleapis.com/css2?family=Cinzel:wght@400;500;600&family=Lora:ital,wght@0,400;0,500;0,600;1,400&display=swap" rel="stylesheet">
<style>
:root{
  --red:#c8070f;
  --red-soft:#d9473f;
  --ink:#1b1a1f;
  --dark:#19171c;
  --grey-bg:#f5f5f5;
  --card-bg:#f7f7f7;
  --muted:#8c8c8c;
  --line:#e6e6e6;
  --white:#ffffff;
  --display:"Cinzel",Georgia,serif;
  --text:"Lora",Georgia,serif;
}
*{box-sizing:border-box;margin:0;padding:0}
html,body{width:1200px;height:3888px;overflow:hidden;background:var(--white)}
body{font-family:var(--text);color:var(--ink);position:relative}
a{color:inherit;text-decoration:none}
.section{position:absolute;left:0;width:1200px}
.abs{position:absolute}

/* top bar */
.topbar{top:0;height:36px;background:#141316;z-index:3}
.toplinks{right:235px;top:10px;display:flex;gap:22px;font:400 11px var(--text);color:#ddd}
.search{right:120px;top:10px;display:flex;align-items:center;gap:6px;font:400 10px var(--text);color:#777}

/* hero */
.hero{top:0;height:738px;overflow:hidden}
.hero-photo{position:absolute;inset:0;background:linear-gradient(100deg,#2a2527 0%,#4a3f40 35%,#3a3436 55%,#221f22 80%,#151315 100%)}
.hero-shade{position:absolute;inset:0;background:rgba(20,18,22,.35)}
.brand{left:40px;top:116px;display:flex;align-items:center;gap:12px}
.brand-square{width:40px;height:40px;background:var(--red)}
.brand-name{font:600 13px var(--display);letter-spacing:3px;color:var(--white)}
.mainnav{left:0;width:1200px;top:140px;display:flex;justify-content:center;gap:30px;font:600 11px var(--display);letter-spacing:2px;color:var(--white)}
.burger{right:42px;top:130px;width:24px}
.burger span{display:block;height:3px;background:#fff;margin-bottom:4px}
.hero-mark{left:0;width:1200px;top:364px;display:flex;justify-content:center;align-items:center;gap:14px}
.hero-mark i{display:block;width:40px;height:1px;background:rgba(255,255,255,.6)}
.hero-title{left:0;width:1200px;top:390px;text-align:center;font:500 40px var(--display);letter-spacing:1px;color:var(--white)}
.hero-title em{font-style:normal;color:var(--red)}
.hero-sub{left:0;width:1200px;top:452px;text-align:center;font:600 8px var(--display);letter-spacing:2px;color:#eee}
.scroll-icon{left:583px;top:565px}

/* headings */
.eyebrow{font:600 10px var(--display);letter-spacing:5px;color:#555}
.title{font:500 48px var(--display);letter-spacing:4px;color:var(--red)}
.intro{font:400 14px var(--text);line-height:24px;letter-spacing:1.5px;text-transform:uppercase;color:var(--muted)}

/* main sections */
.sections{top:738px;height:866px}
.cards{left:160px;top:394px;width:880px;height:345px;display:flex;background:var(--line);gap:2px;padding:2px}
.card{flex:1;background:var(--card-bg);text-align:center;position:relative}
.card-img{margin:16px 14px 0;height:132px;background:linear-gradient(160deg,#e9e9e9,#cfcfcf)}
.card h3{font:500 18px var(--display);margin-top:18px;line-height:22px;color:#222}
.card p{font:400 11px var(--text);line-height:18px;color:#777;margin:16px auto 0;width:160px}
.card .more{position:absolute;left:0;right:0;bottom:22px;font:600 10px var(--display);letter-spacing:4px;color:#222}
.card.is-active{background:var(--red)}
.card.is-active h3,.card.is-active p,.card.is-active .more{color:var(--white)}
.card.is-active .card-img{background:linear-gradient(160deg,#f3eeee,#d8cccc)}

/* best products */
.best{top:1604px;height:975px;background:var(--grey-bg)}
.carousel{left:160px;top:393px;width:880px;height:395px;display:flex;background:var(--white);border:1px solid #ececec}
.slide{flex:1;position:relative;border-right:1px solid #ececec}
.slide-img{position:absolute;inset:40px 20px;background:linear-gradient(160deg,#efefef,#d6d6d6)}
.slide.is-hover{background:#9a9a9a}
.slide.is-hover .slide-img{background:linear-gradient(160deg,#b8b8b8,#8e8e8e)}
.slide-over{position:absolute;inset:0;background:rgba(90,90,90,.45)}
.slide-name{left:26px;top:290px;font:500 16px var(--display);letter-spacing:2px;color:#fff}
.slide-note{left:26px;top:316px;font:400 9px var(--display);letter-spacing:3px;color:#eee}
.slide-price{left:26px;top:350px;font:500 17px var(--display);color:#fff}
.slide-buy{right:30px;top:350px;background:#fff;color:#222;font:600 13px var(--display);letter-spacing:3px;padding:3px 8px}
.dots{left:0;width:1200px;top:830px;display:flex;justify-content:center;gap:22px}
.dots i{width:9px;height:9px;border-radius:50%;background:#ccc}
.dots i.on{background:#333}

/* about */
.about{top:2579px;height:762px;overflow:hidden}
.about-photo{position:absolute;inset:0;background:linear-gradient(110deg,#2c2a2d 0%,#3d393b 40%,#4b4446 65%,#2a2729 100%)}
.about-shade{position:absolute;inset:0;background:rgba(24,22,26,.55)}
.about .eyebrow{color:#ddd}
.about .intro{color:#eee}
.about-copy{left:150px;top:345px;width:660px;font:400 12px var(--text);line-height:20px;color:#bdbdbd}
.about-copy p+p{margin-top:18px}

/* offers band */
.offers{top:3341px;height:92px;background:var(--red);display:flex;align-items:center;justify-content:center;font:600 14px var(--display);letter-spacing:4px;color:#fff}

/* footer */
.footer{top:3433px;height:455px;background:var(--dark)}
.fcol{top:136px;font:400 12px var(--display);letter-spacing:1.5px;line-height:30px;color:#aaa}
.fcol .current{color:var(--red)}
.social{left:617px;top:240px;display:flex;gap:18px}
.social i{width:12px;height:12px;background:var(--red)}
.social i+i{background:#9a9a9a}
.copyright{left:0;width:1200px;top:392px;text-align:center;font:400 11px var(--display);letter-spacing:2px;color:#777}
</style>
</head>
<body>

<header class="section topbar">
  <nav class="abs toplinks"><a href="#">Shipping</a><a href="#">About company</a><a href="#">Contacts</a></nav>
  <div class="abs search">
    <svg width="12" height="12" viewBox="0 0 12 12"><circle cx="5" cy="5" r="3.8" fill="none" stroke="#c8070f" stroke-width="1.4"/><line x1="8" y1="8" x2="11" y2="11" stroke="#c8070f" stroke-width="1.4"/></svg>
    <span>Search...</span>
  </div>
</header>

<section class="section hero">
  <div class="hero-photo" role="img" aria-label="Photo of an elegant mature couple in evening wear, man holding a finger to his lips"></div>
  <div class="hero-shade"></div>
  <div class="abs brand"><span class="brand-square"></span><span class="brand-name">QUIET CHAPTER</span></div>
  <nav class="abs mainnav"><a href="#">HOME</a><a href="#">PRODUCTS</a><a href="#">WEBINARS</a><a href="#">GIFTS</a></nav>
  <div class="abs burger"><span></span><span></span><span></span></div>
  <div class="abs hero-mark"><i></i>
    <svg width="20" height="18" viewBox="0 0 20 18"><path d="M10 17 L2 9 A4.5 4.5 0 0 1 10 3 A4.5 4.5 0 0 1 18 9 Z" fill="#c8070f"/></svg>
  <i></i></div>
  <h1 class="abs hero-title">YOUR <em>DESIRES</em> ARE OUR <em>SECRET</em></h1>
  <div class="abs hero-sub">DISCREET CARE AFTER FIFTY</div>
  <svg class="abs scroll-icon" width="34" height="58" viewBox="0 0 34 58"><rect x="2" y="2" width="30" height="54" rx="15" fill="none" stroke="#fff" stroke-width="2.5"/><line x1="17" y1="12" x2="17" y2="22" stroke="#fff" stroke-width="2.5"/></svg>
</section>

<section class="section sections">
  <div class="abs eyebrow" style="left:150px;top:137px">ONLY THE BEST PRODUCTS</div>
  <h2 class="abs title" style="left:146px;top:172px">THE MAIN SECTIONS</h2>
  <p class="abs intro" style="left:142px;top:248px;width:350px">Thoughtful products and honest advice for a new chapter of life after fifty</p>
  <div class="abs cards">
    <article class="card">
      <div class="card-img" role="img" aria-label="Product photo of a personal massager"></div>
      <h3>MASSAGERS</h3>
      <p>Gentle, easy-to-use designs chosen for comfort at every age</p>
      <a class="more" href="#">VIEW MORE</a>
    </article>
    <article class="card is-active">
      <div class="card-img" role="img" aria-label="Product photo of stockings"></div>
      <h3>INTIMATE<br>APPAREL</h3>
      <p>Elegant lingerie that feels as good as it looks, in every size</p>
      <a class="more" href="#">VIEW MORE</a>
    </article>
    <article class="card">
      <div class="card-img" role="img" aria-label="Product photo of a cream tube"></div>
      <h3>CREAMS</h3>
      <p>Soothing gels and balms made for a changing body</p>
      <a class="more" href="#">VIEW MORE</a>
    </article>
    <article class="card">
      <div class="card-img" role="img" aria-label="Photo of a headset for an online seminar"></div>
      <h3>WEBINARS</h3>
      <p>Private webinars and teleseminars on intimacy and relationships</p>
      <a class="more" href="#">VIEW MORE</a>
    </article>
  </div>
</section>

<section class="section best">
  <div class="abs eyebrow" style="left:150px;top:160px">RECOMMENDATIONS</div>
  <h2 class="abs title" style="left:146px;top:190px;color:var(--red-soft)">THE BEST PRODUCTS</h2>
  <p class="abs intro" style="left:148px;top:266px;width:520px">Favourites chosen by our customers over fifty, delivered in plain packaging</p>
  <div class="abs carousel">
    <div class="slide"><div class="slide-img" role="img" aria-label="Product photo of a massager"></div></div>
    <div class="slide"><div class="slide-img" role="img" aria-label="Product photo of bead accessories"></div></div>
    <div class="slide is-hover">
      <div class="slide-img" role="img" aria-label="Product photo of a cream bottle and box"></div>
      <div class="slide-over"></div>
      <svg class="abs" style="left:84px;top:165px" width="52" height="52" viewBox="0 0 52 52"><circle cx="21" cy="21" r="15" fill="none" stroke="#fff" stroke-width="4"/><line x1="32" y1="32" x2="48" y2="48" stroke="#fff" stroke-width="4"/></svg>
      <div class="abs slide-name">CREAM</div>
      <div class="abs slide-note">SILK TOUCH BALM</div>
      <div class="abs slide-price">$ 150</div>
      <a class="abs slide-buy" href="#">BUY</a>
    </div>
    <div class="slide" style="border-right:0"><div class="slide-img" role="img" aria-label="Product photo of stockings and garter"></div></div>
  </div>
  <div class="abs dots"><i></i><i></i><i class="on"></i></div>
</section>

<section class="section about">
  <div class="about-photo" role="img" aria-label="Dim photo of a mature couple embracing"></div>
  <div class="about-shade"></div>
  <div class="abs eyebrow" style="left:150px;top:144px">SOME INFORMATION</div>
  <h2 class="abs title" style="left:146px;top:176px">ABOUT US</h2>
  <p class="abs intro" style="left:150px;top:252px;width:580px">A private store for people over fifty who are beginning a new phase of life</p>
  <div class="abs about-copy">
    <p>Quiet Chapter supplies intimate products and services for individuals and couples aged fifty and over. Life changes, and so do our needs: bodies, relationships and routines all shift with time. We choose every product for comfort, quality and ease of use, and we explain each one in plain, respectful language. Alongside the store we host webinars and teleseminars where experienced counsellors talk openly about intimacy, health and partnership in later life, so you can listen and learn without ever leaving home.</p>
    <p>Privacy guides everything we do. Our site never shares your details, payments appear under a neutral name, and every order travels in plain, unmarked packaging. From the moment you browse to the day your parcel arrives, the whole process stays between you and us, giving you the freedom to shop and learn in the comfort of your own home.</p>
  </div>
</section>

<a class="section offers" href="#">VIEW SPECIAL OFFERS</a>

<footer class="section footer">
  <nav class="abs fcol" style="left:160px">HOME<br>PRODUCTS<br>BLOG<br>GIFTS</nav>
  <nav class="abs fcol" style="left:388px">SHIPPING<br><span class="current">ABOUT COMPANY</span><br>CONTACTS</nav>
  <address class="abs fcol" style="left:617px;font-style:normal;line-height:26px">011 555 0142<br>HELLO@QUIETCHAPTER.COM<br>18 ELM ROW, WESTBROOK</address>
  <div class="abs social"><i></i><i></i></div>
  <div class="abs copyright">COPYRIGHT ©</div>
</footer>

</body>
</html>
```